Talbrix Business Card Design

We need a modern great looking premium business card design that can be customized by person that also displays a contact QR code. It should match our existing branding and website Talbrix.com . We need to be able to upload it to zell for continued customization and use across a good size company.

```html
<!DOCTYPE html>
<html lang="en">
<head>
<meta charset="utf-8">
<title>Talbrix Business Card</title>
<link rel="stylesheet" href="https://fonts.googleapis.com/css2?family=Lexend:wght@300;400;600&display=swap">
<style>
  :root {
    --brand: #4470b6;
    --paper: #ffffff;
    --stage: #ebebeb;
    --tint: #f2f5fa;
    --ink-light: #ffffff;
  }
  * { margin: 0; padding: 0; box-sizing: border-box; }
  html, body { width: 1200px; height: 1200px; overflow: hidden; }
  body {
    background: var(--stage);
    font-family: "Lexend", sans-serif;
    position: relative;
  }
  .card {
    position: absolute;
    left: 151px;
    width: 895px;
    height: 523px;
    background: var(--paper);
    box-shadow: 0 2px 8px rgba(0,0,0,0.18);
    overflow: hidden;
  }
  .card--front { top: 61px; }
  .card--back { top: 607px; }
  .card__shapes { position: absolute; inset: 0; width: 100%; height: 100%; }

  .brand {
    position: absolute;
    left: 0; right: 0;
    display: flex;
    align-items: center;
    justify-content: center;
    color: var(--brand);
    font-weight: 600;
    line-height: 1;
  }
  .brand__square { background: var(--brand); flex: none; }
  .card--front .brand { top: 88px; font-size: 76px; gap: 34px; }
  .card--front .brand__square { width: 46px; height: 46px; }
  .card--back .brand { top: 215px; font-size: 86px; gap: 44px; }
  .card--back .brand__square { width: 54px; height: 54px; }

  .person {
    position: absolute;
    left: 73px;
    top: 290px;
    color: var(--ink-light);
  }
  .person__name { font-size: 42px; font-weight: 600; line-height: 1; }
  .person__role { font-size: 19px; font-weight: 300; margin-top: 6px; }

  .contact {
    position: absolute;
    right: 95px;
    top: 280px;
    list-style: none;
    color: var(--ink-light);
    font-size: 22px;
    font-weight: 300;
    text-align: right;
  }
  .contact__item {
    display: flex;
    justify-content: flex-end;
    align-items: center;
    gap: 12px;
    height: 29px;
  }
  .contact__icon { width: 15px; height: 15px; flex: none; }

  .qr-code {
    position: absolute;
    left: 44px;
    bottom: 44px;
    width: 112px;
    height: 112px;
    background: var(--tint);
    border: 4px solid var(--brand);
    border-radius: 6px;
  }
</style>
</head>
<body>

<section class="card card--front">
  <svg class="card__shapes" viewBox="0 0 716 418" preserveAspectRatio="none" aria-hidden="true">
    <polygon fill="var(--brand)" points="0,143 353,213 353,303 0,373"/>
    <polygon fill="var(--brand)" points="362,213 716,143 716,373 362,303"/>
    <polygon fill="var(--brand)" points="0,418 39,378 359,313 679,378 716,418"/>
  </svg>

  <div class="brand">
    <span class="brand__square"></span>
    <span class="brand__name">Talbrix</span>
  </div>

  <div class="person">
    <p class="person__name">Marcus Hale</p>
    <p class="person__role">Founder</p>
  </div>

  <ul class="contact">
    <li class="contact__item">
      <span>044 3619 0000</span>
      <svg class="contact__icon" viewBox="0 0 24 24" aria-hidden="true"><path fill="#fff" d="M6.6 10.8a15 15 0 0 0 6.6 6.6l2.2-2.2a1 1 0 0 1 1-.25 11.4 11.4 0 0 0 3.6.57 1 1 0 0 1 1 1V20a1 1 0 0 1-1 1A17 17 0 0 1 3 4a1 1 0 0 1 1-1h3.5a1 1 0 0 1 1 1c0 1.25.2 2.45.57 3.57a1 1 0 0 1-.25 1z"/></svg>
    </li>
    <li class="contact__item">
      <span>talbrix.com</span>
      <svg class="contact__icon" viewBox="0 0 24 24" aria-hidden="true"><path fill="#fff" d="M3 5h18a1 1 0 0 1 1 1v12a1 1 0 0 1-1 1H3a1 1 0 0 1-1-1V6a1 1 0 0 1 1-1zm9 7.5L20 7H4z"/></svg>
    </li>
    <li class="contact__item">
      <span>talbrix.com</span>
      <svg class="contact__icon" viewBox="0 0 24 24" aria-hidden="true"><g fill="none" stroke="#fff" stroke-width="1.8"><circle cx="12" cy="12" r="9.5"/><ellipse cx="12" cy="12" rx="4" ry="9.5"/><path d="M2.5 12h19M4 7h16M4 17h16"/></g></svg>
    </li>
  </ul>
</section>

<section class="card card--back">
  <svg class="card__shapes" viewBox="0 0 716 419" preserveAspectRatio="none" aria-hidden="true">
    <polygon fill="var(--tint)" points="514,0 716,0 716,40 554,40"/>
    <polygon fill="var(--tint)" points="590,96 716,96 716,186 680,186"/>
    <polygon fill="var(--tint)" points="680,240 716,240 716,330 590,330"/>
    <polygon fill="var(--tint)" points="554,383 716,383 716,419 514,419"/>
  </svg>

  <div class="brand">
    <span class="brand__square"></span>
    <span class="brand__name">Talbrix</span>
  </div>

  <div class="qr-code" role="img" aria-label="Contact QR code area"></div>
</section>

</body>
</html>
```